Business Card Project for Firm Deck Hoisting

Business name is "Firm Deck Hoisting" we are a scaffolding & rigging business specialising in local and remote work for:
- scaffolding (residential, commercial, industrial)
- rigging
-man material hoists
- swing stages
- labour hire

On the back of the card I would like FDH as the symbol / logo. I have attached the logos we have had created by sketch harbour. We would like to use bold colours – preferably as the same colour scheme as the logo.

Target Market(s)

Construction business

Industry/Entity Type

Construction

Contact Information for Business Card

name: Owen Pellew
Title: Director
Phone: 0491 572 864
Address: PO BOX 3251, Kestrel Vale SA 5990
Email: owen@firmdeckhoisting.com.au
Website: www.firmdeckhoisting.com.au

Font styles to use
Sans Serif

Requirements
Must have
• Must use existing logo & prefering using bold colours
Nice to have
• Would be nice to have a line of dot points in what we specialise in but not essential
• Would be nice to see some designs with a slogan but not essential
Should not have
• NA

```html
<!DOCTYPE html>
<html lang="en">
<head>
<meta charset="utf-8">
<title>Firm Deck Hoisting – Business Card</title>
<link rel="stylesheet" href="https://fonts.googleapis.com/css2?family=Open+Sans:wght@400;600;700&display=swap">
<style>
  :root {
    --ink: #1c1d20;
    --ink-soft: #26272b;
    --paper: #ffffff;
    --blue: #1f6fc0;
    --grey: #b9bcc2;
    --stage: #2a2c30;
  }
  * { box-sizing: border-box; margin: 0; padding: 0; }
  html, body {
    width: 1200px; height: 900px; overflow: hidden;
    background: var(--stage);
    font-family: "Open Sans", Arial, sans-serif;
  }
  .canvas {
    width: 1200px; height: 900px;
    display: flex; flex-direction: column;
    align-items: center; justify-content: center; gap: 60px;
  }
  .card {
    position: relative; width: 600px; height: 343px;
    border-radius: 22px; overflow: hidden;
    box-shadow: 0 14px 34px rgba(0,0,0,.45);
  }

  /* Front */
  .card--front { background: var(--paper); }
  .front__panel {
    position: absolute; left: 0; top: 0; width: 300px; height: 262px;
    background: var(--ink); padding: 30px 0 0 30px;
  }
  .front__band {
    position: absolute; left: 0; bottom: 0; width: 100%; height: 76px;
    background: var(--blue);
  }
  .front__band-rule {
    position: absolute; left: 0; bottom: 76px; width: 100%; height: 5px;
    background: var(--ink-soft);
  }
  .front__slash {
    position: absolute; left: 86px; bottom: 0; width: 10px; height: 76px;
    background: var(--ink); transform: skewX(-40deg);
  }
  .person { display: flex; gap: 12px; align-items: flex-start; }
  .person__bar { width: 8px; height: 34px; background: var(--blue); margin-top: 2px; }
  .person__name {
    font-size: 22px; font-weight: 600; letter-spacing: .5px;
    color: var(--paper); text-transform: uppercase; line-height: 1.1;
  }
  .person__name .surname { color: var(--blue); }
  .person__title {
    font-size: 11px; font-weight: 600; color: var(--grey);
    text-transform: uppercase; letter-spacing: 1px; margin-top: 3px;
  }
  .contact { list-style: none; margin-top: 22px; }
  .contact__item {
    display: flex; align-items: center; gap: 10px;
    font-size: 11px; color: var(--grey); line-height: 1; margin-bottom: 11px;
    white-space: nowrap;
  }
  .contact__icon { width: 12px; height: 12px; flex: none; }
  .brand {
    position: absolute; display: flex; align-items: center; gap: 10px;
    font-weight: 700; letter-spacing: .5px;
  }
  .brand__mark { width: 14px; height: 14px; background: var(--blue); flex: none; }
  .brand--front { left: 336px; top: 112px; color: var(--ink); }
  .brand__name { font-size: 18px; line-height: 1.25; }
  .brand__initials { font-size: 40px; line-height: 1; display: block; }

  /* Back */
  .card--back { background: var(--ink); }
  .brand--back { left: 50%; top: 112px; transform: translateX(-50%); color: var(--paper); }
  .back__footer {
    position: absolute; left: 0; right: 0; bottom: 28px;
    display: flex; align-items: center; gap: 14px;
  }
  .back__stripe { height: 7px; background: var(--blue); }
  .back__stripe--left { width: 250px; }
  .back__stripe--right { flex: 1; }
  .back__web {
    font-size: 12px; color: var(--grey); letter-spacing: .3px; white-space: nowrap;
  }
</style>
</head>
<body>
<main class="canvas">

  <section class="card card--front" aria-label="Card front">
    <div class="front__panel">
      <div class="person">
        <span class="person__bar"></span>
        <div>
          <p class="person__name">Owen <span class="surname">Pellew</span></p>
          <p class="person__title">Director</p>
        </div>
      </div>
      <ul class="contact">
        <li class="contact__item">
          <svg class="contact__icon" viewBox="0 0 12 12" fill="none" stroke="#b9bcc2" stroke-width="1.1"><path d="M3 1l1.6 2.6-1 1c.6 1.4 1.5 2.3 2.8 2.9l1-1L10 8l-.8 2C5 10 2 7 1.8 2.2z"/></svg>
          0491 572 864
        </li>
        <li class="contact__item">
          <svg class="contact__icon" viewBox="0 0 12 12" fill="none" stroke="#b9bcc2" stroke-width="1.1"><rect x="1" y="2.5" width="10" height="7"/><path d="M1 2.5l5 4 5-4"/></svg>
          owen@firmdeckhoisting.com.au
        </li>
        <li class="contact__item">
          <svg class="contact__icon" viewBox="0 0 12 12" fill="none" stroke="#b9bcc2" stroke-width="1.1"><circle cx="6" cy="6" r="5"/><path d="M1 6h10M6 1c-2.5 3-2.5 7 0 10M6 1c2.5 3 2.5 7 0 10"/></svg>
          www.firmdeckhoisting.com.au
        </li>
        <li class="contact__item">
          <svg class="contact__icon" viewBox="0 0 12 12" fill="none" stroke="#b9bcc2" stroke-width="1.1"><path d="M6 11S2 7 2 4.5a4 4 0 018 0C10 7 6 11 6 11z"/><circle cx="6" cy="4.5" r="1.3"/></svg>
          PO BOX 3251, Kestrel Vale SA 5990
        </li>
      </ul>
    </div>

    <div class="brand brand--front">
      <span class="brand__mark"></span>
      <p class="brand__name"><span class="brand__initials">FDH</span>Firm Deck Hoisting</p>
    </div>

    <div class="front__band-rule"></div>
    <div class="front__band"></div>
    <div class="front__slash"></div>
  </section>

  <section class="card card--back" aria-label="Card back">
    <div class="brand brand--back">
      <span class="brand__mark"></span>
      <p class="brand__name"><span class="brand__initials">FDH</span>Firm Deck Hoisting</p>
    </div>
    <div class="back__footer">
      <div class="back__stripe back__stripe--left"></div>
      <p class="back__web">www.firmdeckhoisting.com.au</p>
      <div class="back__stripe back__stripe--right"></div>
    </div>
  </section>

</main>
</body>
</html>
```